Business card design for Tolvin Waste

I would like double-sided business cards for myself and my partner that includes our logo and the existing colour scheme. We provide waste and environmental services to customers in the motor-vehicle and engineering industries.

```html
<!DOCTYPE html>
<html lang="en">
<head>
<meta charset="utf-8">
<title>Tolvin Waste — Business Card</title>
<link href="https://fonts.googleapis.com/css2?family=Montserrat:wght@400;600&family=Roboto:wght@500&display=swap" rel="stylesheet">
<style>
  :root {
    --backdrop: #262626;
    --card-white: #ffffff;
    --card-dark: #1c1c1c;
    --card-dark-edge: #2c2c2c;
    --brand-green: #6aaa2a;
    --rule-green: #8cc63f;
    --ink: #3a3a3a;
    --logo-grey: #4a4a4a;
    --logo-white: #ffffff;
  }
  * { margin: 0; padding: 0; box-sizing: border-box; }
  html, body {
    width: 1200px; height: 897px; overflow: hidden;
    background: var(--backdrop);
  }
  .canvas { position: relative; width: 1200px; height: 897px; }

  .card {
    position: absolute; left: 304px; width: 594px; height: 338px;
    border-radius: 22px; overflow: hidden;
  }
  .card--front { top: 92px; background: var(--card-white); }
  .card--back {
    top: 470px;
    background: radial-gradient(circle at 80% 75%, var(--card-dark-edge), var(--card-dark) 70%);
  }

  .front-glow {
    position: absolute; right: -40px; top: -10px; width: 320px; height: 320px;
    border-radius: 50%;
    background: radial-gradient(circle, #f6f6f6 0%, #fbfbfb 55%, rgba(255,255,255,0) 70%);
  }

  .holder { position: absolute; left: 36px; top: 30px; }
  .holder__name {
    font-family: "Roboto", sans-serif; font-weight: 500;
    font-size: 24px; color: var(--brand-green); line-height: 1.1;
  }
  .holder__role {
    font-family: "Montserrat", sans-serif; font-weight: 400;
    font-size: 16px; color: var(--ink); margin-top: 2px;
  }

  .rule {
    position: absolute; left: 36px; width: 30px; height: 2px;
    background: var(--rule-green);
  }
  .rule--one { top: 102px; }
  .rule--two { top: 204px; }

  .address {
    position: absolute; left: 36px; top: 136px;
    font-family: "Montserrat", sans-serif; font-size: 16.5px;
    color: var(--ink); line-height: 20px; font-style: normal;
  }

  .contacts {
    position: absolute; left: 36px; top: 240px; list-style: none;
    font-family: "Montserrat", sans-serif; font-size: 16.5px;
    color: var(--ink); line-height: 20px;
  }
  .contacts li { display: flex; align-items: center; gap: 8px; }
  .contacts svg { width: 11px; height: 11px; flex: none; }

  .wordmark {
    position: absolute; display: flex; align-items: center;
    font-family: "Montserrat", sans-serif; font-weight: 600;
  }
  .wordmark__dot { border-radius: 50%; background: var(--brand-green); flex: none; }
  .wordmark__name { line-height: 1; letter-spacing: 1px; }

  .wordmark--front { left: 316px; top: 226px; gap: 14px; }
  .wordmark--front .wordmark__dot { width: 62px; height: 62px; }
  .wordmark--front .wordmark__name { font-size: 30px; color: var(--logo-grey); }

  .wordmark--back { left: 134px; top: 120px; gap: 20px; }
  .wordmark--back .wordmark__dot { width: 92px; height: 92px; }
  .wordmark--back .wordmark__name { font-size: 42px; color: var(--logo-white); }
</style>
</head>
<body>
<main class="canvas">

  <section class="card card--front" aria-label="Card front">
    <div class="front-glow"></div>

    <div class="holder">
      <p class="holder__name">Morgan Hale</p>
      <p class="holder__role">Director</p>
    </div>

    <div class="rule rule--one"></div>

    <address class="address">
      14 Wattlebrook Road<br>
      KELDARA NSW 2609
    </address>

    <div class="rule rule--two"></div>

    <ul class="contacts">
      <li>
        <svg viewBox="0 0 12 12" aria-hidden="true"><path d="M3 1 L5 3.5 L4 5 Q5 7.5 7 8 L8.5 7 L11 9 L9.5 11 Q3 10 1 2.5 Z" fill="none" stroke="#6aaa2a" stroke-width="1.2" stroke-linejoin="round"/></svg>
        (123) 555-0148
      </li>
      <li>
        <svg viewBox="0 0 12 12" aria-hidden="true"><rect x="1" y="2.5" width="10" height="7" fill="none" stroke="#6aaa2a" stroke-width="1.2"/><path d="M1 2.5 L6 6.5 L11 2.5" fill="none" stroke="#6aaa2a" stroke-width="1.2"/></svg>
        info@tolvinwaste.com
      </li>
      <li>
        <svg viewBox="0 0 12 12" aria-hidden="true"><circle cx="6" cy="6" r="5" fill="none" stroke="#6aaa2a" stroke-width="1.1"/><ellipse cx="6" cy="6" rx="2.2" ry="5" fill="none" stroke="#6aaa2a" stroke-width="1"/><path d="M1 6 H11 M2 3.5 H10 M2 8.5 H10" stroke="#6aaa2a" stroke-width="0.9"/></svg>
        www.tolvinwaste.com
      </li>
    </ul>

    <div class="wordmark wordmark--front">
      <span class="wordmark__dot"></span>
      <span class="wordmark__name">TOLVIN<br>WASTE</span>
    </div>
  </section>

  <section class="card card--back" aria-label="Card back">
    <div class="wordmark wordmark--back">
      <span class="wordmark__dot"></span>
      <span class="wordmark__name">TOLVIN<br>WASTE</span>
    </div>
  </section>

</main>
</body>
</html>
```